Tri fold brochure for construction company

Looking for a tri fold brochure which utilizes black, teal and white colors. Logo must be on main page (several files with Logo attached)
Inside brochure.
1st Page - 3D photo/sketch/drawing of a complete residential high rise building with windows, balconies and elements of concrete and bricks.
2nd Page - Text which will outline company's main activities. file with text is attached.
3rd Page - photo/sketch/drawing of underground parking garage which shows columns/beams/walls/ and garage entrance/exit ramp. Can be multiple photos.
Back of brochure
1st page - company logo
2nd page - please propose something.
3rd page - company message with address and contact info (to be provided)
Back ground color of brochure should complement our logo/photos/sketches/drawings.
Alternative design options are welcome.

```html
<!DOCTYPE html>
<html lang="en">
<head>
<meta charset="utf-8">
<title>Norvale Restoration Corp. – Tri-fold Brochure</title>
<link href="https://fonts.googleapis.com/css2?family=Lato:wght@400;700;900&display=swap" rel="stylesheet">
<style>
  :root {
    --canvas: #3c3c3c;
    --teal: #1fa78c;
    --teal-dark: #178a73;
    --charcoal: #333333;
    --slate: #4f4f4f;
    --slate-mid: #565656;
    --ink: #222222;
    --white: #ffffff;
    --paper: #f1f1f1;
  }
  * { margin: 0; padding: 0; box-sizing: border-box; }
  html, body { width: 786px; height: 1200px; overflow: hidden; }
  body {
    background: var(--canvas);
    font-family: "Lato", Arial, sans-serif;
    color: var(--white);
    position: relative;
  }
  .sheet { position: absolute; left: 53px; width: 681px; height: 528px; overflow: hidden; }
  .sheet--outside { top: 58px; background: linear-gradient(135deg, #ffffff 40%, #dcdcdc 100%); }
  .sheet--inside { top: 614px; background: var(--charcoal); }
  .block { position: absolute; }
  .photo { position: absolute; }

  /* ---------- outside ---------- */
  .misc-panel { left: 0; top: 0; width: 222px; height: 274px; background: var(--slate); }
  .misc-edge { left: 222px; top: 0; width: 8px; height: 290px; background: #c9c9c9; }
  .misc-title { position: absolute; left: 24px; top: 33px; font-size: 17px; font-weight: 700; letter-spacing: .2px; }
  .misc-list { position: absolute; left: 24px; top: 66px; width: 192px; list-style: none; font-size: 9.6px; line-height: 10.4px; }
  .misc-list li { margin-bottom: 8.6px; padding-left: 8px; position: relative; }
  .misc-list li::before { content: "•"; position: absolute; left: 0; }

  .photo--villa { left: 230px; top: 0; width: 221px; height: 290px;
    background: radial-gradient(ellipse at 50% 45%, #7f8ea8 0%, #b6c2d4 40%, #eef1f5 72%, #ffffff 100%); }

  .brand { left: 451px; top: 40px; width: 230px; text-align: center; color: var(--ink); font-weight: 900; }
  .brand-square { width: 54px; height: 54px; background: var(--teal); margin: 0 auto 26px; }
  .brand-name { font-size: 27px; line-height: 28px; letter-spacing: .5px; }
  .brand-sub { font-size: 11.5px; line-height: 16px; letter-spacing: .4px; }

  .row-dark { left: 0; top: 290px; width: 240px; height: 238px; background: var(--slate); }
  .photo--tower { left: 0; top: 290px; width: 208px; height: 238px;
    background: linear-gradient(160deg, #8d939c 0%, #3f6fb8 35%, #1f4f9f 70%, #163f86 100%);
    clip-path: polygon(0 0, 100% 0, 88% 100%, 0 100%); }
  .tower-gap { left: 196px; top: 290px; width: 20px; height: 238px; background: #d8d8d8;
    clip-path: polygon(60% 0, 100% 0, 40% 100%, 0 100%); }

  .contact { left: 227px; top: 290px; width: 223px; height: 238px; background: var(--teal); }
  .contact-name { position: absolute; top: 56px; width: 100%; text-align: center; font-size: 20px; font-weight: 900; letter-spacing: 1px; }
  .contact-title { position: absolute; top: 101px; width: 100%; text-align: center; font-size: 15px; font-weight: 700; }
  .contact-list { position: absolute; left: 52px; top: 130px; list-style: none; font-size: 9px; line-height: 11.8px; }
  .contact-list li { position: relative; padding-left: 16px; }
  .contact-list li + li { margin-top: 0; }
  .contact-list .gap { margin-top: 3px; }
  .contact-list svg { position: absolute; left: 0; top: 2px; width: 9px; height: 9px; }

  .strip-dark { left: 450px; top: 290px; width: 34px; height: 238px; background: var(--slate); }
  .photo--sketch-house { left: 478px; top: 258px; width: 203px; height: 270px;
    background: linear-gradient(120deg, #ffffff 0%, #f2f2f2 35%, #a0724d 55%, #e9e9e9 75%, #c7d9a9 100%);
    clip-path: polygon(40% 0, 100% 0, 100% 100%, 4% 100%, 0 18%); }

  /* ---------- inside ---------- */
  .teal-back { left: 229px; top: 0; width: 240px; height: 178px; background: var(--teal); }
  .photo--red-house { left: 0; top: 0; width: 265px; height: 178px;
    background: linear-gradient(100deg, #f4f4f4 0%, #d93a30 25%, #e6e6e6 50%, #ffffff 100%);
    clip-path: polygon(0 0, 100% 0, 86% 100%, 0 100%); }
  .photo--blue-house { left: 229px; top: 0; width: 226px; height: 178px;
    background: linear-gradient(180deg, #6f9fd6 0%, #e3ebf3 40%, #b9c5cf 70%, #5c7fa8 100%);
    clip-path: polygon(20% 0, 93% 0, 86% 100%, 0 100%); }
  .photo--architect { left: 455px; top: 0; width: 226px; height: 262px;
    background: linear-gradient(135deg, #c7d3d4 0%, #8aa3a5 35%, #4f6466 60%, #d4dcdc 100%); }

  .envelope-band { left: 0; top: 178px; width: 229px; height: 92px; background: var(--slate-mid); }
  .photo--garage { left: 229px; top: 178px; width: 226px; height: 92px;
    background: linear-gradient(180deg, #6f7377 0%, #b9bcbf 45%, #8d9195 100%); }

  .teal-panel { position: absolute; left: 0; top: 0; }
  .photo--garage-sketch { left: 243px; top: 434px; width: 164px; height: 94px;
    background: linear-gradient(120deg, #ffffff 0%, #ececec 40%, #e8c23a 60%, #f5f5f5 100%);
    clip-path: polygon(0 0, 100% 0, 93% 100%, 0 100%); }

  .section-title { position: absolute; font-size: 16.5px; font-weight: 700; line-height: 20px; letter-spacing: .1px; }
  .sub { font-size: 9.6px; font-weight: 700; text-transform: uppercase; line-height: 12px; }
  .list { list-style: none; font-size: 9.4px; line-height: 12px; }
  .list li { position: relative; padding-left: 8px; }
  .list li::before { content: "•"; position: absolute; left: 0; }
  .text-block { position: absolute; }
</style>
</head>
<body>

<!-- Outside spread -->
<section class="sheet sheet--outside">
  <div class="block misc-panel">
    <h2 class="misc-title">MISCELLANEOUS:</h2>
    <ul class="misc-list">
      <li>Railings remediation and replacement</li>
      <li>Outside garbage pad enclosures</li>
      <li>Retaining walls repair/replacement</li>
      <li>Weeping tile systems</li>
      <li>Safety bollards &amp; precast curbs installation</li>
      <li>Side walks, curbs, interlocking, asphalt and concrete pads</li>
      <li>Balconies and Parking garages painting</li>
      <li>Area drains replacements</li>
      <li>Etc.</li>
    </ul>
  </div>
  <div class="block misc-edge"></div>
  <div class="photo photo--villa" role="img" aria-label="Rendering of a modern white villa with glass walls and a reflecting pool"></div>

  <div class="block brand">
    <div class="brand-square"></div>
    <div class="brand-name">NORVALE</div>
    <div class="brand-sub">RESTORATION CORP.</div>
  </div>

  <div class="block row-dark"></div>
  <div class="block tower-gap"></div>
  <div class="photo photo--tower" role="img" aria-label="High-rise residential building rendering blending into a blue blueprint wireframe"></div>

  <div class="block contact">
    <div class="contact-name">NORVALE</div>
    <h3 class="contact-title">Contats Us</h3>
    <ul class="contact-list">
      <li>
        <svg viewBox="0 0 10 10"><path d="M5 1 L9.5 5 H8 V9 H2 V5 H.5 Z" fill="#fff"/></svg>
        Address Line here<br>Your City, State, Zip Code,<br>Country
      </li>
      <li>
        <svg viewBox="0 0 10 10"><circle cx="5" cy="5" r="4.4" fill="none" stroke="#fff" stroke-width="1"/><path d="M3.4 2.8 L4.3 2.6 L4.8 3.9 L4.2 4.4 Q4.8 5.6 5.7 5.9 L6.2 5.3 L7.4 5.8 L7.2 6.7 Q5.2 7.2 3.4 2.8 Z" fill="#fff"/></svg>
        +00 000 000 0000
      </li>
      <li class="gap">
        <svg viewBox="0 0 10 10"><circle cx="5" cy="5" r="4.4" fill="none" stroke="#fff" stroke-width="1"/><rect x="2.6" y="3.4" width="4.8" height="3.3" fill="none" stroke="#fff" stroke-width=".8"/><path d="M2.6 3.4 L5 5.3 L7.4 3.4" fill="none" stroke="#fff" stroke-width=".8"/></svg>
        mail@yourwebsite.com
      </li>
      <li class="gap">
        <svg viewBox="0 0 10 10"><circle cx="5" cy="5" r="4.4" fill="none" stroke="#fff" stroke-width="1"/><circle cx="5" cy="5" r="2.4" fill="none" stroke="#fff" stroke-width=".8"/><path d="M2.6 5 H7.4 M5 2.6 V7.4" stroke="#fff" stroke-width=".6"/></svg>
        www.yourwebsite.com
      </li>
    </ul>
  </div>

  <div class="block strip-dark"></div>
  <div class="photo photo--sketch-house" role="img" aria-label="Half-sketched, half-rendered modern house with wood cladding and garage"></div>
</section>

<!-- Inside spread -->
<section class="sheet sheet--inside">
  <div class="block teal-back"></div>
  <div class="photo photo--blue-house" role="img" aria-label="Modern white house rendering fading into a blue sketch"></div>
  <div class="photo photo--red-house" role="img" aria-label="Red modern house rendering transitioning into a pencil sketch"></div>
  <div class="photo photo--architect" role="img" aria-label="Hand drawing a sketch of an underground garage interior"></div>

  <div class="block envelope-band"></div>
  <div class="photo photo--garage" role="img" aria-label="Empty underground parking garage with columns and lights"></div>

  <svg class="teal-panel" width="681" height="528" viewBox="0 0 681 528" aria-hidden="true">
    <polygon points="446,264 681,264 681,528 405,528" fill="var(--teal)"/>
    <polygon points="455,264 459,264 420,528 416,528" fill="var(--white)"/>
  </svg>
  <div class="photo photo--garage-sketch" role="img" aria-label="Line drawing of a parking garage with yellow-marked columns and cars"></div>

  <h2 class="section-title" style="left:26px; top:184px;">BUILDING ENVELOPE:</h2>
  <div class="text-block" style="left:26px; top:212px;">
    <div class="sub">Concrete Repairs</div>
    <ul class="list" style="margin-top:2px;">
      <li>Balcony slabs</li>
      <li>Shear Walls</li>
      <li>Beams &amp; Columns</li>
    </ul>
  </div>

  <div class="text-block" style="left:26px; top:280px; width:220px;">
    <div class="sub">Masonry Repairs</div>
    <ul class="list" style="margin-top:10px;">
      <li>Brick, Block &amp; Stone replacement</li>
      <li>Tuck pointing</li>
      <li>Through wall flashing</li>
      <li>Coating (Sealer, Elastomeric,<br>Silicone and Architectural coatings)</li>
    </ul>
    <div class="sub" style="margin-top:10px;">Sealant Replacement</div>
    <ul class="list" style="margin-top:10px;">
      <li>Window wall and glazing system sealants</li>
      <li>Precast sealants</li>
      <li>Masonry sealants</li>
      <li>Balcony perimeter joints</li>
    </ul>
    <div class="sub" style="margin-top:9px;">Waterproofing</div>
    <ul class="list" style="margin-top:10px;">
      <li>Balconies &amp; Terraces thin system</li>
      <li>Garbage &amp; Mechanical rooms</li>
    </ul>
  </div>

  <h2 class="section-title" style="left:246px; top:275px;">PARKING GARAGE<br>STRUCTURES:</h2>
  <div class="text-block" style="left:248px; top:323px; width:170px;">
    <div class="sub">Concrete Repairs</div>
    <ul class="list" style="margin-top:7px;">
      <li>Partial slab replacement</li>
      <li>Top/under side repairs</li>
      <li>Hydro demolition</li>
      <li>Columns, Beams and Shear Walls</li>
      <li>Catch basins &amp; trench drains</li>
      <li>Staircases</li>
    </ul>
  </div>

  <div class="text-block" style="left:481px; top:306px; width:190px;">
    <div class="sub">Waterproofing</div>
    <ul class="list" style="margin-top:7px;">
      <li>Vehicular thin system (drive aisles,<br>parking bays, ramps, etc.)</li>
      <li>Hot applied waterproofing<br>(Ramps and Roof decks)</li>
      <li>Expansion joints repairs/replacement</li>
      <li>Mastic waterproofing system</li>
      <li>Foundation wall crack injections</li>
      <li>Crystalline waterproofing</li>
    </ul>
    <div class="sub" style="margin-top:7px;">Ramp Remediation</div>
    <ul class="list" style="margin-top:7px;">
      <li>Electric heating cables</li>
      <li>Asphalt, Interlocking,<br>Mastic and Concrete</li>
    </ul>
  </div>
</section>

</body>
</html>
```